Need a FLAT UI design for mobile campus Marketplace APP

We need to improve our current UI/UX design for a mobile application called Tradlo. It is designed for students to buy and sell their goods, such as books and furnitures, on their own campus to save living expenses. Our initial design does not look very flat and clear enough. We would like to see a flat design improvement for a better purchasing and selling experience using yellow as theme color.

Target Market(s)

college students

Industry/Entity Type

Marketplace

Colors
ffc214
ffcf3e
fee18a
fff3d1

Requirements
Must have
• an improved UI look, flat and simple.
Nice to have
• alternative designs
Should not have
• a new function design for the app on the design

```html
<!DOCTYPE html>
<html lang="en">
<head>
<meta charset="utf-8">
<title>Tradlo — campus marketplace screens</title>
<link rel="stylesheet" href="https://fonts.googleapis.com/css2?family=Open+Sans:wght@400;600;700&display=swap">
<style>
  :root{
    --page:#dcdcdc;
    --bar:#ffd84a;
    --bar-active:#ffe98f;
    --stripe:#ffb81c;
    --cream:#fff3c8;
    --white:#ffffff;
    --ink:#1d1d1d;
    --muted:#6d6d6d;
    --faint:#c9c9c9;
    --orange:#ff9812;
    --blue:#40a2e3;
    --teal:#2ea79b;
    --magenta:#d556b7;
    --purple:#8671b1;
    --brown:#a46e46;
    --red:#e5233d;
    --black:#111111;
    --button:#35a89e;
  }
  *{box-sizing:border-box;margin:0;padding:0}
  html,body{width:1200px;height:2192px;overflow:hidden}
  body{background:var(--page);font-family:"Open Sans",Arial,sans-serif;color:var(--ink);position:relative}

  .screen{position:absolute;width:540px;height:960px;background:var(--cream);overflow:hidden}
  .screen--home{left:40px;top:90px}
  .screen--chat{left:620px;top:90px}
  .screen--post{left:40px;top:1142px}
  .screen--profile{left:620px;top:1142px}

  .pattern{position:absolute;left:0;top:107px;width:540px;height:853px;
    background:radial-gradient(ellipse at 50% 40%,#fff6d6 0%,var(--cream) 70%)}

  .topbar{position:absolute;left:0;top:0;width:540px;height:108px;background:var(--bar)}
  .status{position:absolute;left:0;top:0;width:540px;height:22px;font-size:13px;display:flex;align-items:center;justify-content:space-between;padding:0 14px}
  .status__carrier{display:flex;align-items:center;gap:6px}
  .status__dots{display:flex;gap:2px}
  .status__dots i{width:7px;height:7px;border-radius:50%;background:var(--ink);display:block}
  .status__dots i:last-child{background:none;border:1px solid var(--ink)}
  .status__battery{display:flex;align-items:center;gap:6px}
  .battery{width:30px;height:12px;border:1px solid var(--ink);padding:1px;position:relative}
  .battery::before{content:"";display:block;width:100%;height:100%;background:var(--ink)}
  .battery::after{content:"";position:absolute;right:-4px;top:3px;width:2px;height:5px;background:var(--ink)}

  .search{position:absolute;left:20px;top:44px;width:500px;height:50px;background:var(--white);border-radius:25px;display:flex;align-items:center;justify-content:space-between;padding:0 20px;font-size:17px;font-style:italic;color:var(--muted)}
  .title{position:absolute;left:0;top:50px;width:540px;text-align:center;font-size:23px;color:var(--ink)}
  .back{position:absolute;left:18px;top:46px}
  .mypost{position:absolute;right:20px;top:48px;border:2px solid var(--ink);border-radius:8px;font-size:16px;font-weight:600;padding:3px 10px}

  .brand{position:absolute;left:0;top:230px;width:540px;text-align:center}
  .brand__mark{width:80px;height:80px;border-radius:50%;background:var(--ink);margin:0 auto 14px}
  .brand__name{font-size:50px;font-weight:700;color:var(--ink)}

  .tile{position:absolute;color:var(--white);display:flex;align-items:center;justify-content:center;font-weight:600}
  .tile svg{position:absolute;top:12px;right:16px}
  .tile--campus{background:var(--orange)}
  .tile--electronics{background:var(--blue)}
  .tile--recent{background:var(--teal)}
  .tile--books{background:var(--magenta)}
  .tile--tickets{background:var(--purple)}
  .tile--others{background:var(--brown)}
  .home-tile{width:180px;height:162px;font-size:21px}
  .post-tile{width:270px;height:253px;font-size:27px}
  .post-tile svg{top:18px;right:22px}

  .stripe{position:absolute;left:0;top:866px;width:540px;height:8px;background:var(--stripe)}
  .nav{position:absolute;left:0;top:874px;width:540px;height:86px;background:var(--bar);display:flex}
  .nav__item{flex:1;display:flex;flex-direction:column;align-items:center;justify-content:center;gap:4px;font-size:11px;font-weight:700;position:relative}
  .nav__item--active{background:var(--bar-active)}
  .badge{position:absolute;background:var(--red);color:var(--white);border-radius:50%;font-size:12px;font-weight:700;display:flex;align-items:center;justify-content:center;width:22px;height:22px}
  .nav .badge{top:10px;left:60px}

  .chat-row{position:absolute;left:20px;width:500px;height:113px;background:var(--white);display:flex;align-items:center}
  .avatar{width:108px;height:108px;border-radius:50%;flex:none;margin-left:4px}
  .avatar--rider{background:linear-gradient(160deg,#e7eef2 10%,#9fb2a4 55%,#4f7c93 100%)}
  .avatar--portrait{background:linear-gradient(160deg,#2c4f6e 0%,#c99c7c 50%,#3b4a6a 100%)}
  .chat-row__text{margin-left:18px;flex:1}
  .chat-row__name{font-size:22px;font-weight:600}
  .chat-row__msg{font-size:16px;color:#3a3a3a}
  .chat-row__time{font-size:14px;font-style:italic;color:var(--faint);margin-right:20px}
  .chat-row .badge{left:4px;top:4px;width:28px;height:28px;font-size:15px}

  .activation{position:absolute;left:0;top:108px;width:540px;height:56px;display:flex;font-weight:700}
  .activation__state{background:var(--black);color:var(--white);font-size:15px;display:flex;align-items:center;justify-content:center;clip-path:polygon(0 0,100% 0,86% 100%,0 100%);width:172px;padding-right:20px}
  .activation__resend{flex:1;background:var(--red);color:var(--white);font-size:16px;display:flex;align-items:center;justify-content:center;gap:10px;margin-left:-20px}

  .profile-photo{position:absolute;left:147px;top:222px;width:246px;height:246px;border-radius:50%;border:10px solid var(--bar);background:linear-gradient(160deg,#2c4f6e 0%,#c99c7c 50%,#3b4a6a 100%)}
  .camera{position:absolute;left:330px;top:408px;width:64px;height:64px;border-radius:50%;background:var(--orange);border:5px solid var(--bar);display:flex;align-items:center;justify-content:center}
  .email{position:absolute;left:0;top:490px;width:540px;text-align:center;font-size:19px;color:var(--muted)}
  .field{position:absolute;left:40px;width:460px;height:76px;background:var(--white);display:flex;align-items:center;padding:0 22px;gap:16px;font-size:23px}
  .field__req{margin-left:auto;color:var(--faint);font-size:24px}
  .save{position:absolute;left:40px;top:806px;width:460px;height:90px;border-radius:18px;background:var(--button);color:var(--white);font-size:22px;font-weight:700;display:flex;align-items:center;justify-content:center}
</style>
</head>
<body>

<!-- Home -->
<section class="screen screen--home">
  <div class="pattern" role="img" aria-label="Faint doodle pattern of school supplies"></div>
  <header class="topbar">
    <div class="status"><span class="status__carrier"><span class="status__dots"><i></i><i></i><i></i><i></i><i></i></span>Carrier</span><span>5:30PM</span><span class="status__battery">100% <span class="battery"></span></span></div>
    <div class="search"><span>Search...</span>
      <svg width="26" height="26" viewBox="0 0 24 24" fill="none" stroke="#1d1d1d" stroke-width="2.6"><circle cx="10" cy="10" r="7"/><path d="M15 15l6 6"/></svg>
    </div>
  </header>
  <div class="brand">
    <div class="brand__mark"></div>
    <div class="brand__name">Tradlo</div>
  </div>
  <div class="tile tile--campus home-tile" style="left:0;top:544px">
    <svg width="34" height="30" viewBox="0 0 24 22" fill="#fff"><path d="M12 0L1 5v2h22V5z"/><rect x="3" y="8" width="3" height="9"/><rect x="8" y="8" width="3" height="9"/><rect x="13" y="8" width="3" height="9"/><rect x="18" y="8" width="3" height="9"/><rect x="1" y="18" width="22" height="3"/></svg>
    Campus Life</div>
  <div class="tile tile--electronics home-tile" style="left:180px;top:544px">
    <svg width="32" height="30" viewBox="0 0 24 22" fill="none" stroke="#fff" stroke-width="2.4"><rect x="2" y="2" width="20" height="13"/><path d="M8 20h8M12 15v5"/></svg>
    Electronics</div>
  <div class="tile tile--recent home-tile" style="left:360px;top:544px">
    <svg width="30" height="30" viewBox="0 0 22 22" fill="#fff"><rect x="1" y="1" width="9" height="9"/><rect x="12" y="1" width="9" height="9"/><rect x="1" y="12" width="9" height="9"/><rect x="12" y="12" width="9" height="9"/></svg>
    Recent</div>
  <div class="tile tile--books home-tile" style="left:0;top:706px">
    <svg width="36" height="28" viewBox="0 0 26 20" fill="none" stroke="#fff" stroke-width="2.2"><path d="M13 4C10 1 5 1 2 2v16c3-1 8-1 11 2 3-3 8-3 11-2V2c-3-1-8-1-11 2zM13 4v16"/></svg>
    Books</div>
  <div class="tile tile--tickets home-tile" style="left:180px;top:706px">
    <svg width="34" height="34" viewBox="0 0 24 24" fill="none" stroke="#fff" stroke-width="2.2"><path d="M4 12L12 4l3 3a2 2 0 003 3l3 3-8 8-3-3a2 2 0 00-3-3z"/></svg>
    Tickets</div>
  <div class="tile tile--others home-tile" style="left:360px;top:706px">
    <svg width="34" height="34" viewBox="0 0 24 24" fill="none" stroke="#fff" stroke-width="2"><circle cx="12" cy="12" r="10"/><circle cx="7.5" cy="12" r="1.4" fill="#fff"/><circle cx="12" cy="12" r="1.4" fill="#fff"/><circle cx="16.5" cy="12" r="1.4" fill="#fff"/></svg>
    Others</div>
  <div class="stripe"></div>
  <nav class="nav">
    <div class="nav__item nav__item--active"><svg width="40" height="36" viewBox="0 0 24 22" fill="none" stroke="#1d1d1d" stroke-width="1.8"><path d="M2 11L12 2l10 9M5 9v11h5v-6h4v6h5V9"/></svg>HOME</div>
    <div class="nav__item"><svg width="40" height="36" viewBox="0 0 24 22" fill="none" stroke="#1d1d1d" stroke-width="1.8"><path d="M4 7h15l-4-4M20 15H5l4 4"/></svg>TRADE</div>
    <div class="nav__item"><svg width="40" height="36" viewBox="0 0 24 22" fill="none" stroke="#1d1d1d" stroke-width="1.8"><path d="M13 3H3v17h17V10"/><path d="M9 14l1-4 9-9 3 3-9 9z"/></svg>POST</div>
    <div class="nav__item"><span class="badge">3</span><svg width="40" height="36" viewBox="0 0 24 22" fill="none" stroke="#1d1d1d" stroke-width="1.8"><path d="M2 3h20v13H9l-5 4v-4H2z"/><circle cx="7" cy="9.5" r="1" fill="#1d1d1d"/><circle cx="12" cy="9.5" r="1" fill="#1d1d1d"/><circle cx="17" cy="9.5" r="1" fill="#1d1d1d"/></svg>CHAT</div>
    <div class="nav__item"><svg width="40" height="36" viewBox="0 0 24 22" fill="none" stroke="#1d1d1d" stroke-width="1.8"><circle cx="12" cy="6" r="5"/><path d="M3 21c0-5 4-8 9-8s9 3 9 8z"/></svg>ACCOUNT</div>
  </nav>
</section>

<!-- Chat -->
<section class="screen screen--chat">
  <div class="pattern" role="img" aria-label="Faint doodle pattern of school supplies"></div>
  <header class="topbar">
    <div class="status"><span class="status__carrier"><span class="status__dots"><i></i><i></i><i></i><i></i><i></i></span>Carrier</span><span>5:30PM</span><span class="status__battery">100% <span class="battery"></span></span></div>
    <svg class="back" width="24" height="40" viewBox="0 0 12 20" fill="none" stroke="#1d1d1d" stroke-width="1.6"><path d="M10 1L2 10l8 9"/></svg>
    <div class="title">CHAT</div>
  </header>
  <div class="chat-row" style="top:141px"><span class="badge">3</span><div class="avatar avatar--rider" role="img" aria-label="Profile photo of David skateboarding"></div><div class="chat-row__text"><div class="chat-row__name">David</div><div class="chat-row__msg">Do you take a card?</div></div><span class="chat-row__time">20:24</span></div>
  <div class="chat-row" style="top:268px"><div class="avatar avatar--portrait" role="img" aria-label="Profile photo of Jays"></div><div class="chat-row__text"><div class="chat-row__name">Jays</div><div class="chat-row__msg">I'll meet you tomorrow.</div></div><span class="chat-row__time">20:24</span></div>
  <div class="chat-row" style="top:395px"><div class="avatar avatar--rider" role="img" aria-label="Profile photo of David skateboarding"></div><div class="chat-row__text"><div class="chat-row__name">David</div><div class="chat-row__msg">Do you take a card?</div></div><span class="chat-row__time">20:24</span></div>
  <div class="chat-row" style="top:522px"><div class="avatar avatar--portrait" role="img" aria-label="Profile photo of Jays"></div><div class="chat-row__text"><div class="chat-row__name">Jays</div><div class="chat-row__msg">I'll meet you tomorrow.</div></div><span class="chat-row__time">20:24</span></div>
  <div class="chat-row" style="top:649px"><div class="avatar avatar--rider" role="img" aria-label="Profile photo of David skateboarding"></div><div class="chat-row__text"><div class="chat-row__name">David</div><div class="chat-row__msg">Do you take a card?</div></div><span class="chat-row__time">20:24</span></div>
  <div class="stripe"></div>
  <nav class="nav">
    <div class="nav__item"><svg width="40" height="36" viewBox="0 0 24 22" fill="none" stroke="#1d1d1d" stroke-width="1.8"><path d="M2 11L12 2l10 9M5 9v11h5v-6h4v6h5V9"/></svg>HOME</div>
    <div class="nav__item"><svg width="40" height="36" viewBox="0 0 24 22" fill="none" stroke="#1d1d1d" stroke-width="1.8"><path d="M4 7h15l-4-4M20 15H5l4 4"/></svg>TRADE</div>
    <div class="nav__item"><svg width="40" height="36" viewBox="0 0 24 22" fill="none" stroke="#1d1d1d" stroke-width="1.8"><path d="M13 3H3v17h17V10"/><path d="M9 14l1-4 9-9 3 3-9 9z"/></svg>POST</div>
    <div class="nav__item nav__item--active"><span class="badge">3</span><svg width="40" height="36" viewBox="0 0 24 22" fill="none" stroke="#1d1d1d" stroke-width="1.8"><path d="M2 3h20v13H9l-5 4v-4H2z"/><circle cx="7" cy="9.5" r="1" fill="#1d1d1d"/><circle cx="12" cy="9.5" r="1" fill="#1d1d1d"/><circle cx="17" cy="9.5" r="1" fill="#1d1d1d"/></svg>CHAT</div>
    <div class="nav__item"><svg width="40" height="36" viewBox="0 0 24 22" fill="none" stroke="#1d1d1d" stroke-width="1.8"><circle cx="12" cy="6" r="5"/><path d="M3 21c0-5 4-8 9-8s9 3 9 8z"/></svg>ACCOUNT</div>
  </nav>
</section>

<!-- Post items -->
<section class="screen screen--post">
  <div class="pattern" role="img" aria-label="Faint doodle pattern of school supplies"></div>
  <header class="topbar">
    <div class="status"><span class="status__carrier"><span class="status__dots"><i></i><i></i><i></i><i></i><i></i></span>Carrier</span><span>5:30PM</span><span class="status__battery">100% <span class="battery"></span></span></div>
    <svg class="back" width="24" height="40" viewBox="0 0 12 20" fill="none" stroke="#1d1d1d" stroke-width="1.6"><path d="M10 1L2 10l8 9"/></svg>
    <div class="title">POST ITEMS</div>
    <div class="mypost">My Post</div>
  </header>
  <div class="tile tile--campus post-tile" style="left:0;top:108px">
    <svg width="54" height="48" viewBox="0 0 24 22" fill="#fff"><path d="M12 0L1 5v2h22V5z"/><rect x="3" y="8" width="3" height="9"/><rect x="8" y="8" width="3" height="9"/><rect x="13" y="8" width="3" height="9"/><rect x="18" y="8" width="3" height="9"/><rect x="1" y="18" width="22" height="3"/></svg>
    Campus Life</div>
  <div class="tile tile--electronics post-tile" style="left:270px;top:108px">
    <svg width="52" height="48" viewBox="0 0 24 22" fill="none" stroke="#fff" stroke-width="2.4"><rect x="2" y="2" width="20" height="13"/><path d="M8 20h8M12 15v5"/></svg>
    Electronics</div>
  <div class="tile tile--books post-tile" style="left:0;top:361px">
    <svg width="58" height="44" viewBox="0 0 26 20" fill="none" stroke="#fff" stroke-width="2.2"><path d="M13 4C10 1 5 1 2 2v16c3-1 8-1 11 2 3-3 8-3 11-2V2c-3-1-8-1-11 2zM13 4v16"/></svg>
    Books</div>
  <div class="tile tile--tickets post-tile" style="left:270px;top:361px">
    <svg width="54" height="54" viewBox="0 0 24 24" fill="none" stroke="#fff" stroke-width="2.2"><path d="M4 12L12 4l3 3a2 2 0 003 3l3 3-8 8-3-3a2 2 0 00-3-3z"/></svg>
    Tickets</div>
  <div class="tile tile--others post-tile" style="left:0;top:614px">
    <svg width="52" height="52" viewBox="0 0 24 24" fill="none" stroke="#fff" stroke-width="2"><circle cx="12" cy="12" r="10"/><circle cx="7.5" cy="12" r="1.4" fill="#fff"/><circle cx="12" cy="12" r="1.4" fill="#fff"/><circle cx="16.5" cy="12" r="1.4" fill="#fff"/></svg>
    Others</div>
  <div class="stripe"></div>
  <nav class="nav">
    <div class="nav__item"><svg width="40" height="36" viewBox="0 0 24 22" fill="none" stroke="#1d1d1d" stroke-width="1.8"><path d="M2 11L12 2l10 9M5 9v11h5v-6h4v6h5V9"/></svg>HOME</div>
    <div class="nav__item"><svg width="40" height="36" viewBox="0 0 24 22" fill="none" stroke="#1d1d1d" stroke-width="1.8"><path d="M4 7h15l-4-4M20 15H5l4 4"/></svg>TRADE</div>
    <div class="nav__item nav__item--active"><svg width="40" height="36" viewBox="0 0 24 22" fill="none" stroke="#1d1d1d" stroke-width="1.8"><path d="M13 3H3v17h17V10"/><path d="M9 14l1-4 9-9 3 3-9 9z"/></svg>POST</div>
    <div class="nav__item"><span class="badge">3</span><svg width="40" height="36" viewBox="0 0 24 22" fill="none" stroke="#1d1d1d" stroke-width="1.8"><path d="M2 3h20v13H9l-5 4v-4H2z"/><circle cx="7" cy="9.5" r="1" fill="#1d1d1d"/><circle cx="12" cy="9.5" r="1" fill="#1d1d1d"/><circle cx="17" cy="9.5" r="1" fill="#1d1d1d"/></svg>CHAT</div>
    <div class="nav__item"><svg width="40" height="36" viewBox="0 0 24 22" fill="none" stroke="#1d1d1d" stroke-width="1.8"><circle cx="12" cy="6" r="5"/><path d="M3 21c0-5 4-8 9-8s9 3 9 8z"/></svg>ACCOUNT</div>
  </nav>
</section>

<!-- Edit information -->
<section class="screen screen--profile">
  <div class="pattern" role="img" aria-label="Faint doodle pattern of school supplies"></div>
  <header class="topbar">
    <div class="status"><span class="status__carrier"><span class="status__dots"><i></i><i></i><i></i><i></i><i></i></span>Carrier</span><span>5:30PM</span><span class="status__battery">100% <span class="battery"></span></span></div>
    <svg class="back" width="24" height="40" viewBox="0 0 12 20" fill="none" stroke="#1d1d1d" stroke-width="1.6"><path d="M10 1L2 10l8 9"/></svg>
    <div class="title">EDIT INFORMATION</div>
  </header>
  <div class="activation">
    <div class="activation__state">Not Activated</div>
    <div class="activation__resend">
      <svg width="30" height="26" viewBox="0 0 24 20" fill="#fff"><path d="M0 9L24 0l-5 20-7-6-3 5v-7L20 3 7 11z"/></svg>
      RESEND ACTIVATION EMAIL</div>
  </div>
  <div class="profile-photo" role="img" aria-label="Profile photo of Jays"></div>
  <div class="camera"><svg width="30" height="24" viewBox="0 0 24 20" fill="#fff"><path d="M2 5h5l2-3h6l2 3h5v14H2z"/><circle cx="12" cy="11.5" r="4" fill="#ff9812"/></svg></div>
  <div class="email">jays.campus@tradlo.com</div>
  <div class="field" style="top:538px"><svg width="24" height="24" viewBox="0 0 24 24" fill="none" stroke="#b5b5b5" stroke-width="1.6"><circle cx="12" cy="7" r="5"/><path d="M3 23c0-5 4-8 9-8s9 3 9 8z"/></svg>Jays<span class="field__req">*</span></div>
  <div class="field" style="top:622px"><svg width="24" height="26" viewBox="0 0 24 26" fill="none" stroke="#b5b5b5" stroke-width="1.6"><path d="M12 25S3 15 3 9a9 9 0 0118 0c0 6-9 16-9 16z"/><circle cx="12" cy="9" r="3"/></svg>Love Library</div>
  <div class="field" style="top:709px"><svg width="24" height="24" viewBox="0 0 24 24" fill="none" stroke="#b5b5b5" stroke-width="1.6"><path d="M3 21l2-6L17 3l4 4L9 19zM15 5l4 4"/></svg>Descriptions</div>
  <div class="save">SAVE</div>
</section>

</body>
</html>
```